Saucy Velvet Impz Business Card

We need business cards designed for our consultants to use and hand out to customers.
We are an Adult party plan company (like Crelvaware but sex toys and lingerie)
We would like bright colours pinks, purples.
The cards need our logo
Space for the reps phone number email address and name.
We need our website on it www.saucyvelvetimps.com.au

```html
<!DOCTYPE html>
<html lang="en">
<head>
<meta charset="UTF-8">
<title>Saucy Velvet Impz Business Card</title>
<link href="https://fonts.googleapis.com/css2?family=Lobster&family=Montserrat:wght@300;400;800&display=swap" rel="stylesheet">
<style>
  :root {
    --page: #efeae6;
    --plum-dark: #1f0c1c;
    --plum: #5a1a4f;
    --magenta: #a0307f;
    --glow: #c8559e;
    --pink-soft: #e7b8d8;
    --pink-text: #d46fb3;
    --white: #ffffff;
    --edge: #2a0d25;
  }
  * { margin: 0; padding: 0; box-sizing: border-box; }
  html, body { width: 1200px; height: 1000px; overflow: hidden; }
  body {
    background: var(--page);
    position: relative;
    font-family: "Montserrat", sans-serif;
  }
  .card {
    position: absolute;
    left: 320px;
    width: 560px;
    height: 320px;
    border-radius: 18px;
    overflow: hidden;
    box-shadow: 0 10px 30px rgba(40, 10, 35, 0.35);
    background:
      radial-gradient(ellipse 55% 70% at 55% 45%, var(--glow) 0%, var(--magenta) 35%, var(--plum) 70%, var(--plum-dark) 100%);
  }
  .card-front { top: 130px; }
  .card-back { top: 540px; }
  .bokeh {
    position: absolute;
    border-radius: 50%;
    background: rgba(255, 200, 235, 0.08);
  }
  .front-brand {
    position: absolute;
    left: 0; right: 0; top: 118px;
    text-align: center;
  }
  .brand-name {
    font-family: "Lobster", sans-serif;
    font-size: 44px;
    color: var(--white);
    line-height: 1;
  }
  .brand-mark {
    display: inline-block;
    width: 14px; height: 14px;
    border-radius: 50%;
    background: var(--white);
    margin-right: 12px;
    vertical-align: middle;
    position: relative;
    top: -6px;
  }
  .tagline {
    margin-top: 10px;
    font-weight: 300;
    font-size: 15px;
    letter-spacing: 0.5px;
    color: var(--pink-soft);
  }
  .rep-name {
    position: absolute;
    left: 34px; top: 28px;
    font-weight: 800;
    text-transform: uppercase;
    line-height: 1;
  }
  .rep-first { display: block; font-size: 36px; color: var(--pink-soft); }
  .rep-last { display: block; font-size: 32px; color: var(--white); margin-top: 2px; }
  .rep-title {
    display: block;
    margin-top: 6px;
    font-weight: 300;
    font-size: 13px;
    color: var(--pink-soft);
    text-transform: none;
  }
  .contact-list {
    position: absolute;
    left: 34px; top: 150px;
    list-style: none;
    font-size: 13px;
    color: var(--white);
  }
  .contact-list li {
    display: flex;
    align-items: center;
    gap: 10px;
    margin-bottom: 9px;
  }
  .contact-list svg { width: 12px; height: 12px; fill: var(--white); flex: none; }
  .back-brand {
    position: absolute;
    left: 34px; bottom: 26px;
    font-family: "Lobster", sans-serif;
    font-size: 24px;
    color: var(--pink-text);
  }
  .figure-area {
    position: absolute;
    right: 0; bottom: 0;
    width: 240px; height: 300px;
    border-top-left-radius: 120px;
    background: linear-gradient(160deg, rgba(240, 205, 230, 0.75), rgba(215, 150, 200, 0.45));
  }
</style>
</head>
<body>
  <section class="card card-front">
    <span class="bokeh" style="left:60px; top:200px; width:70px; height:70px;"></span>
    <span class="bokeh" style="left:420px; top:40px; width:90px; height:90px;"></span>
    <div class="front-brand">
      <span class="brand-mark"></span><span class="brand-name">Saucy Velvet Impz</span>
      <p class="tagline">Australia's No 1 Adult Party Plan</p>
    </div>
  </section>

  <section class="card card-back">
    <span class="bokeh" style="left:260px; top:60px; width:110px; height:110px;"></span>
    <span class="bokeh" style="left:130px; top:230px; width:60px; height:60px;"></span>
    <div class="figure-area" role="img" aria-label="Pale pink seated figure silhouette decoration"></div>
    <h1 class="rep-name">
      <span class="rep-first">Marla</span>
      <span class="rep-last">Quenneville</span>
      <span class="rep-title">President</span>
    </h1>
    <ul class="contact-list">
      <li>
        <svg viewBox="0 0 24 24"><path d="M6.6 10.8a15.5 15.5 0 0 0 6.6 6.6l2.2-2.2a1 1 0 0 1 1-.25 11.4 11.4 0 0 0 3.6.57 1 1 0 0 1 1 1V20a1 1 0 0 1-1 1A17 17 0 0 1 3 4a1 1 0 0 1 1-1h3.5a1 1 0 0 1 1 1c0 1.25.2 2.45.57 3.57a1 1 0 0 1-.25 1z"/></svg>
        +32 400 55 18 27
      </li>
      <li>
        <svg viewBox="0 0 24 24"><path d="M2 5h20v14H2z M2 5l10 8 10-8" fill="none" stroke="#fff" stroke-width="2"/></svg>
        marla@saucyvelvetimps.com.au
      </li>
      <li>
        <svg viewBox="0 0 24 24"><circle cx="12" cy="12" r="9" fill="none" stroke="#fff" stroke-width="2"/><path d="M3 12h18M12 3c3 3 3 15 0 18M12 3c-3 3-3 15 0 18" fill="none" stroke="#fff" stroke-width="1.5"/></svg>
        www.saucyvelvetimps.com.au
      </li>
    </ul>
    <p class="back-brand">Saucy Velvet Impz</p>
  </section>
</body>
</html>
```